Website - freeride bike clothing company

Need a complete website with eCommerce.
Company: A new brand of bike (freeride) clothing...not the lycra stuff!

I have a design concept I have put together in Illustrator (see screen shots attached and below is a link to drop box with the full file - it was too heavy to attach here). The drop box folder also has images to use in the demo site. Refer to:
1) Landing Page - front page with images
2) Website - each subsequent page
3) Images folder
4) Logo for the website
https://www.filecrate-share.com/sh/k82pq7dm3xwa5/T9Lm4vQpzB

The above is my vision. Any design tips/suggestions to make it better are welcome. I want it to be easy to use and navigate and it needs to look RAD!

I do actually have a word press version of this with the first page already set up - if this can help?
I would like it up and running in 2 weeks (??), if possible.

I need to be able to turn on and off pages as I like, add products easily, team members etc.

I need eCommerce set up:
1) Direct to the public with pricing, shopping cart, online payment, shipping etc.
2) Wholesaler login. Same structure as public but I would need to pre-approve and set up any wholesalers to access this section, and it has different pricing.
I want to be able to turn on/off either of the above, ie: I might only use one or the other at one time.

Inspiration sites:
http://www.quellor.com/au/en/womens/
http://au.brindlefox.com/home.php
www.tarnvelomade.com

Site pages:
1) HOME - Landing Page

2) Gear
2a) Ladies / Mens / Other (each it's own page, same format, I can add new categories anytime)
2a(i) Item specific drill down

3) Crew
3a) Drill down per team member

4) Happenings
4a) News / Events
4b) Media
4c) Adventures
4d) Videos

5) Customer Service
5a) Policies / FAQ
5b) Size Chart
5c) Material
5d) Store Locator
5e) Contact

6) Shopping cart / check out and wholesaler login section

Target Market(s)

Extreme sports 25 - 40 year olds.
Men and women.
It is mostly a mens sport, but I am making womens gear too.

Industry/Entity Type

Clothing

Requirements
Must have
• Funky cool way to showcase my clothing products
Cool, simple yet professional look
Easily viewable photos of the product - easy to scroll between shots and to enlarge where needed.
Link to facebook and social media for the news sections, liking etc.
Crew section - link to that specific persons feed ie: on facebook/instagram

Pages:
1) Home Page

2) Gear
2a) Ladies / Mens / Other (same format pages - can add catagories as I like)
2ab) Item Specific Drill Down
2abc) Shopping Cart

3) Crew landing
3a) Crew Drill Down per person

4) Happenings
4a) News / Events / Media / Adventures / Videos

5) Customer Service
5a) Policies / FAQs
5ab) Size Chart
5abc) Material

6) Store Locator

7) Shopping Cart - both direct to public and a wholesale login section (I need to be able to grant people access and a login to the wholesale section)
Possibility to add promo codes to make things cheaper for specific people or sale time etc...

```html
<!DOCTYPE html>
<html lang="en">
<head>
<meta charset="utf-8">
<title>KRELVO — Freeride Clothing</title>
<link rel="stylesheet" href="https://fonts.googleapis.com/css2?family=Arimo:wght@400;700&family=Gelasio:wght@400;500&display=swap">
<style>
  :root {
    --page-bg: #f9f9f9;
    --ink: #111111;
    --nav-ink: #2b2b2b;
    --tab-bg: #a3a3a3;
    --white: #ffffff;
    --panel-dark: #0b0b0b;
    --team-green: #3fe33b;
  }
  * { box-sizing: border-box; margin: 0; padding: 0; }
  html, body {
    width: 1100px;
    height: 1200px;
    overflow: hidden;
    background: var(--page-bg);
  }
  .site { position: relative; width: 1100px; height: 1200px; }

  /* Header */
  .brand {
    position: absolute;
    left: 67px;
    top: 22px;
    display: flex;
    align-items: center;
    gap: 10px;
    font-family: "Arimo", sans-serif;
    font-weight: 700;
    font-size: 34px;
    letter-spacing: -1px;
    color: var(--ink);
  }
  .brand-mark { width: 36px; height: 36px; background: var(--ink); }
  .main-nav {
    position: absolute;
    left: 270px;
    top: 0;
    display: flex;
    height: 88px;
    font-family: "Arimo", sans-serif;
    font-weight: 700;
    font-size: 12px;
    text-transform: uppercase;
  }
  .main-nav a {
    display: flex;
    align-items: center;
    padding: 0 15px;
    color: var(--nav-ink);
    text-decoration: none;
    height: 88px;
  }
  .main-nav a.is-active {
    position: relative;
    width: 100px;
    justify-content: center;
    padding: 0;
    background: var(--tab-bg);
    color: var(--white);
  }
  .main-nav a.is-active::before {
    content: "";
    position: absolute;
    top: 0;
    left: 47px;
    border-left: 3px solid transparent;
    border-right: 3px solid transparent;
    border-top: 3px solid var(--page-bg);
  }

  /* Hero */
  .hero {
    position: absolute;
    left: 71px;
    top: 123px;
    width: 960px;
    height: 300px;
    background:
      radial-gradient(ellipse 38% 30% at 30% 38%, rgba(255,214,120,0.75) 0%, rgba(255,190,90,0) 100%),
      radial-gradient(ellipse 30% 22% at 82% 26%, rgba(255,200,110,0.55) 0%, rgba(255,200,110,0) 100%),
      radial-gradient(ellipse 55% 30% at 62% 78%, rgba(120,130,30,0.85) 0%, rgba(120,130,30,0) 100%),
      radial-gradient(ellipse 25% 14% at 80% 98%, rgba(60,50,40,0.9) 0%, rgba(60,50,40,0) 100%),
      linear-gradient(180deg, #b8520f 0%, #e08a28 30%, #d47a24 46%, #9c4516 56%, #8a4a18 66%, #6f6a1e 82%, #4e6416 100%);
  }

  /* Tile grid */
  .tile {
    position: absolute;
    width: 299px;
    height: 230px;
    overflow: hidden;
    text-decoration: none;
  }
  .photo { box-shadow: inset 0 0 60px rgba(0,0,0,0.35); }
  .tile-label {
    position: absolute;
    font-family: "Gelasio", serif;
    font-size: 18px;
    color: var(--white);
    text-shadow: 0 1px 2px rgba(0,0,0,0.35);
  }
  .tile-label.top-left { left: 8px; top: 6px; }
  .tile-label.top-right { right: 14px; top: 6px; }
  .tile-label.bottom-left { left: 22px; bottom: 30px; }

  .info-panel {
    background: radial-gradient(ellipse at 50% 40%, #272727 0%, var(--panel-dark) 78%);
    color: var(--white);
    font-family: "Gelasio", serif;
    padding: 11px 17px 0;
  }
  .info-panel h2 {
    font-weight: 400;
    font-size: 24px;
    text-align: center;
    margin-bottom: 19px;
  }
  .info-panel p {
    font-size: 13.3px;
    font-weight: 500;
    line-height: 17px;
    margin-bottom: 16px;
  }
  .info-panel.team { color: var(--team-green); padding-top: 13px; }
  .info-panel.team h2 { padding-left: 12px; margin-bottom: 22px; }

  .col-1 { left: 71px; }
  .col-2 { left: 405px; }
  .col-3 { left: 739px; }
  .row-1 { top: 498px; }
  .row-2 { top: 764px; }
  .row-3 { top: 1030px; }

  .photo-bicycle {
    width: 298px;
    background:
      radial-gradient(ellipse 45% 35% at 38% 22%, rgba(255,230,190,0.85) 0%, rgba(255,220,180,0) 100%),
      radial-gradient(ellipse 40% 45% at 50% 72%, rgba(90,40,60,0.55) 0%, rgba(90,40,60,0) 100%),
      linear-gradient(170deg, #d8b2a4 0%, #b77684 45%, #8c4e68 75%, #6a3a55 100%);
  }
  .photo-mens {
    width: 298px;
    background:
      radial-gradient(ellipse 35% 35% at 42% 22%, rgba(30,60,140,0.9) 0%, rgba(30,60,140,0) 100%),
      radial-gradient(ellipse 40% 35% at 62% 72%, rgba(40,120,190,0.9) 0%, rgba(40,120,190,0) 100%),
      radial-gradient(ellipse 25% 25% at 88% 72%, rgba(200,40,50,0.85) 0%, rgba(200,40,50,0) 100%),
      linear-gradient(90deg, #8a8f92 0%, #6f7478 40%, #9a9ea0 100%);
  }
  .photo-rider-portrait {
    background:
      radial-gradient(ellipse 30% 28% at 18% 30%, rgba(150,190,70,0.55) 0%, rgba(150,190,70,0) 100%),
      radial-gradient(ellipse 28% 25% at 55% 25%, rgba(40,40,40,0.9) 0%, rgba(40,40,40,0) 100%),
      radial-gradient(ellipse 22% 20% at 55% 50%, rgba(200,150,120,0.7) 0%, rgba(200,150,120,0) 100%),
      radial-gradient(ellipse 45% 30% at 52% 92%, rgba(110,150,150,0.85) 0%, rgba(110,150,150,0) 100%),
      linear-gradient(160deg, #4d6d24 0%, #2e4418 50%, #1e2c12 100%);
  }
  .photo-events {
    width: 300px;
    background:
      radial-gradient(ellipse 18% 14% at 52% 15%, rgba(240,240,240,0.85) 0%, rgba(240,240,240,0) 100%),
      radial-gradient(ellipse 32% 28% at 50% 50%, rgba(40,70,170,0.9) 0%, rgba(40,70,170,0) 100%),
      radial-gradient(ellipse 22% 24% at 65% 75%, rgba(230,180,40,0.7) 0%, rgba(230,180,40,0) 100%),
      linear-gradient(170deg, #2a4a24 0%, #1d3318 50%, #12200e 100%);
  }
  .photo-ladies {
    width: 300px;
    background:
      radial-gradient(ellipse 40% 45% at 92% 25%, rgba(255,190,80,0.9) 0%, rgba(255,190,80,0) 100%),
      radial-gradient(ellipse 25% 30% at 25% 65%, rgba(60,140,60,0.6) 0%, rgba(60,140,60,0) 100%),
      radial-gradient(ellipse 30% 30% at 55% 60%, rgba(190,50,40,0.55) 0%, rgba(190,50,40,0) 100%),
      linear-gradient(110deg, #3a2418 0%, #7a3a22 40%, #b8602a 75%, #d88a3a 100%);
  }
  .photo-team-rider {
    width: 300px;
    background:
      radial-gradient(ellipse 35% 40% at 45% 55%, rgba(40,80,190,0.9) 0%, rgba(40,80,190,0) 100%),
      radial-gradient(ellipse 18% 18% at 78% 40%, rgba(30,30,40,0.8) 0%, rgba(30,30,40,0) 100%),
      linear-gradient(160deg, #b5a47a 0%, #8c8060 45%, #6a6050 100%);
  }
  .photo-videos {
    width: 300px;
    background:
      radial-gradient(ellipse 40% 40% at 62% 30%, rgba(40,40,40,0.95) 0%, rgba(40,40,40,0) 100%),
      radial-gradient(ellipse 45% 40% at 55% 85%, rgba(10,10,10,0.95) 0%, rgba(10,10,10,0) 100%),
      radial-gradient(ellipse 18% 22% at 95% 20%, rgba(220,180,160,0.8) 0%, rgba(220,180,160,0) 100%),
      linear-gradient(160deg, #d2d2d2 0%, #a8a8a8 45%, #5a5a5a 100%);
  }
</style>
</head>
<body>
<div class="site">
  <header>
    <div class="brand"><span class="brand-mark"></span>KRELVO</div>
    <nav class="main-nav">
      <a href="#" class="is-active">Homepage</a>
      <a href="#">Gear</a>
      <a href="#">Crew</a>
      <a href="#">Happenings</a>
      <a href="#">Customer Service</a>
      <a href="#">Store Locator</a>
      <a href="#">Shopping Cart</a>
    </nav>
  </header>

  <main>
    <div class="hero" role="img" aria-label="Freeride rider jumping a bike over mountains at sunset"></div>

    <section class="tile info-panel col-1 row-1" style="width:298px">
      <h2>THE GEAR</h2>
      <p>Lorem ipsum dolor sit amet, ad usu unum iudico consequuntur.</p>
      <p>Consulatu vulputate nam ad, inani denique pertinacia est ex. Agam intellegat an eos, et nominavi disputationi per.</p>
      <p>Pro ferri veniam vulputate id. An sumo noluisse hendrerit sea,</p>
    </section>

    <div class="tile photo photo-bicycle col-2 row-1" role="img" aria-label="Rider on a sunlit city street with hand lettered bicycle slogan"></div>

    <a class="tile photo photo-mens col-3 row-1" href="#" role="img" aria-label="Rider in helmet and jersey from the mens range">
      <span class="tile-label top-right">Mens Range</span>
    </a>

    <a class="tile photo photo-rider-portrait col-1 row-2" href="#" role="img" aria-label="Portrait of crew rider in a cap outdoors">
      <span class="tile-label top-left">Julien Marcel</span>
    </a>

    <a class="tile photo photo-events col-2 row-2" href="#" role="img" aria-label="Downhill racer riding through a forest at an event">
      <span class="tile-label bottom-left">Events</span>
    </a>

    <a class="tile photo photo-ladies col-3 row-2" href="#" role="img" aria-label="Group of riders in goggles and helmets from the ladies range">
      <span class="tile-label top-left" style="left:14px">Ladies Range</span>
    </a>

    <section class="tile info-panel team col-1 row-3" style="width:300px">
      <h2>THE TEAM</h2>
      <p>Lorem ipsum dolor sit amet, ad usu unum iudico consequuntur, consulatu vulputate nam ad, inani denique pertinacia est ex.</p>
      <p>Agam intellegat an eos, et nominavi dispu-<br>tationi per.</p>
    </section>

    <a class="tile photo photo-team-rider col-2 row-3" href="#" role="img" aria-label="Team rider cornering on a bike in full gear">
      <span class="tile-label top-left" style="left:14px">Bree Halloran</span>
    </a>

    <a class="tile photo photo-videos col-3 row-3" href="#" role="img" aria-label="Hand holding a video camera">
      <span class="tile-label top-left" style="left:10px">Videos</span>
    </a>
  </main>
</div>
</body>
</html>
```